New more attractive design for an old tired look that is high tech but inviting

Need a more modern eye catching design. We are and I/T and MSP and we need a new look. Need a call to action on each page. Needs to be in WordPress. Existing site is brivanoqe.com. Needs to work on phones and tablets. The default home page should present us as an MSP/MSSP and direct the viewer to our services we offer.
Updates

Current deadline assigned at project inception has passed before project started

Need extra days to review

Target Market(s)

Our target market is other businesses. We do not target residential customers.

Industry/Entity Type

Business to Business oriented

Coding

Coded - Design and coding required

Number of Pages Required

5+ page

Font styles to use
Sans Serif

Requirements
Must have
• Must have a current relevant design with a call to action on each page.
Nice to have
• Dark background high tech look with people to make it attractive

```html
<!DOCTYPE html>
<html lang="en">
<head>
<meta charset="utf-8">
<title>Brivanoq Tech – IT Solutions That Power Your Business</title>
<link rel="stylesheet" href="https://fonts.googleapis.com/css2?family=Poppins:wght@400;500;600;700&display=swap">
<style>
:root{
  --red:#e01f26;
  --red-deep:#c8101a;
  --ink:#2e3a44;
  --text:#4a4f55;
  --muted:#6b7077;
  --grey:#eeeff1;
  --footer:#2f3e4a;
  --white:#ffffff;
}
*{box-sizing:border-box;margin:0;padding:0}
html,body{width:1200px;height:3256px;overflow:hidden}
body{font-family:'Poppins',sans-serif;color:var(--text);background:var(--white);position:relative}
.abs{position:absolute}
.btn{position:absolute;display:flex;align-items:center;justify-content:center;gap:10px;font-size:9.5px;font-weight:500;letter-spacing:.3px;text-transform:uppercase;text-decoration:none}
.btn-red{background:var(--red);color:var(--white)}
.btn-white{background:var(--white);color:var(--ink)}
.dashes{position:absolute}
h1,h2,h3{font-weight:600;color:var(--ink)}

/* header */
.site-header{position:absolute;left:0;top:0;width:1200px;height:60px;background:var(--white);box-shadow:0 1px 4px rgba(0,0,0,.05);z-index:2}
.brand{position:absolute;left:95px;top:14px;display:flex;align-items:center;gap:7px;font-size:22px;font-weight:600;color:var(--ink)}
.brand .mark{width:9px;height:9px;background:var(--red)}
.main-nav{position:absolute;left:682px;top:21px;display:flex;gap:32px;font-size:11px;color:var(--ink);align-items:center}
.phone{position:absolute;left:978px;top:12px;display:flex;align-items:center;gap:12px;font-size:11px;font-weight:600;color:var(--ink)}
.phone .ring{width:36px;height:36px;border-radius:50%;background:#fbe4e5;display:flex;align-items:center;justify-content:center}

/* hero */
.hero{position:absolute;left:0;top:60px;width:1200px;height:547px;background:linear-gradient(180deg,#fbe3e5 0%,#fdf3f4 45%,#ffffff 100%)}
.hero h1{position:absolute;left:91px;top:187px;font-size:42px;line-height:44px;font-weight:600}
.hero p{position:absolute;left:93px;top:280px;font-size:14.5px;line-height:21px;color:var(--text)}
.hero-photo{position:absolute;left:589px;top:126px;width:479px;height:406px;background:linear-gradient(160deg,#8a8577 0%,#5d5a52 45%,#3d3a3a 100%)}
.badge{position:absolute;left:1019px;top:199px;width:109px;height:107px;background:var(--red);color:var(--white);text-align:center;padding-top:27px}
.badge strong{display:block;font-size:28px;font-weight:600;line-height:32px}
.badge span{font-size:8.5px}

/* expertise */
.expertise{position:absolute;left:24px;top:628px;width:1152px;height:549px;background:var(--red);overflow:hidden}
.expertise h2{position:absolute;left:68px;top:72px;font-size:32px;line-height:37px;color:var(--white)}
.service-card{position:absolute;top:181px;width:246px;height:285px;background:var(--white);padding:0 30px 0 35px}
.service-card.featured{background:linear-gradient(180deg,#4a5f70 0%,#2f4455 100%)}
.service-card svg.icon{position:absolute;left:33px;top:32px}
.service-card h3{position:absolute;left:35px;top:105px;font-size:15px;line-height:19px;color:var(--ink)}
.service-card p{position:absolute;left:35px;top:148px;width:185px;font-size:10.5px;line-height:16px;color:var(--text)}
.service-card .rule{position:absolute;left:22px;right:26px;top:234px;height:1px;background:#cfd1d4}
.service-card .more{position:absolute;left:0;right:0;top:252px;text-align:center;font-size:12px;color:var(--ink)}
.service-card.featured h3,.service-card.featured p,.service-card.featured .more{color:var(--white)}
.service-card.featured .rule{background:rgba(255,255,255,.35)}

/* about */
.about h2{position:absolute;left:166px;top:1252px;font-size:33px;color:var(--ink)}
.about-photo{position:absolute;left:166px;top:1358px;width:869px;height:407px;background:linear-gradient(100deg,#1f2a35 0%,#3b4652 40%,#7a5346 75%,#3a3b44 100%)}
.about-text{position:absolute;left:166px;top:1834px;width:462px;font-size:12.2px;line-height:19px;color:var(--text)}
.about-box{position:absolute;left:663px;top:1788px;width:372px;height:244px;background:var(--grey);padding:47px 36px 0 45px;font-size:12.2px;line-height:19px;color:var(--text)}
.red-line{position:absolute;height:3px;background:var(--red)}

/* data center */
.dc-band{position:absolute;left:0;top:2152px;width:1200px;height:219px;background:var(--grey)}
.dc-band h2{position:absolute;left:166px;top:88px;font-size:33px}
.dc-band p{position:absolute;left:166px;top:137px;font-size:12.5px}
.dc-photo{position:absolute;left:0;top:2371px;width:525px;height:479px;background:linear-gradient(120deg,#5a0d12 0%,#a11a20 35%,#1d3a44 70%,#0e1d24 100%)}
.feature{position:absolute;left:593px;width:515px}
.feature .circ{position:absolute;left:0;top:0;width:74px;height:74px;border-radius:50%;background:var(--grey);display:flex;align-items:center;justify-content:center}
.feature h3{position:absolute;left:90px;top:0;font-size:15px}
.feature p{position:absolute;left:90px;top:24px;width:425px;font-size:10.4px;line-height:16px;color:var(--text)}

/* quote */
.quote{position:absolute;left:94px;top:2795px;width:1106px;height:189px;background:linear-gradient(90deg,var(--red-deep) 0%,var(--red) 100%)}
.quote h2{position:absolute;left:81px;top:65px;font-size:33px;color:var(--white)}
.quote p{position:absolute;left:81px;top:115px;font-size:12.2px;color:var(--white)}

/* footer */
.site-footer{position:absolute;left:0;top:2984px;width:1200px;height:272px;background:var(--footer);color:var(--white)}
.footer-brand{position:absolute;left:105px;top:83px;display:flex;align-items:center;gap:10px;font-size:40px;font-weight:600;color:var(--white)}
.footer-brand .mark{width:12px;height:12px;background:var(--red)}
.footer-nav{position:absolute;right:97px;top:96px;display:flex;gap:14px;font-size:12.5px}
.footer-contact{position:absolute;right:97px;top:116px;text-align:left;font-size:12.5px;line-height:20px}
.footer-contact div{display:flex;align-items:center;gap:6px}
.footer-rule{position:absolute;left:92px;right:92px;top:224px;height:1px;background:rgba(255,255,255,.2)}
.copyright{position:absolute;left:92px;top:240px;font-size:12px}
.legal{position:absolute;right:97px;top:240px;font-size:12px;display:flex;gap:14px}
.to-top{position:absolute;left:1131px;top:197px;width:34px;height:34px;border-radius:50%;background:var(--red);display:flex;align-items:center;justify-content:center}
</style>
</head>
<body>

<header class="site-header">
  <div class="brand"><span class="mark"></span>Brivanoq Tech</div>
  <nav class="main-nav">
    <svg width="12" height="11" viewBox="0 0 12 11"><path d="M6 0L0 5h1.5v6h3.5V7.5h2V11h3.5V5H12z" fill="#e01f26"/></svg>
    <span>SERVICES</span><span>ABOUT</span><span>CONTACT</span>
  </nav>
  <div class="phone">
    <span class="ring"><svg width="15" height="14" viewBox="0 0 15 14"><path d="M2 9V7a5.5 5.5 0 0111 0v2" fill="none" stroke="#e01f26" stroke-width="1.6"/><rect x="1" y="8" width="3" height="5" rx="1" fill="#e01f26"/><rect x="11" y="8" width="3" height="5" rx="1" fill="#e01f26"/></svg></span>
    555-013-4827
  </div>
</header>

<section class="hero">
  <h1>IT Solutions That<br>Power Your Business</h1>
  <p>Managed Services, Cybersecurity, and 24/7 Support<br>Tailored to Fit Your Business Needs.</p>
  <a class="btn btn-red" style="left:94px;top:337px;width:142px;height:34px">Get a free IT audit
    <svg width="10" height="7" viewBox="0 0 10 7"><path d="M0 3.5h9M6 .5l3 3-3 3" fill="none" stroke="#fff"/></svg></a>
  <svg class="dashes" style="left:70px;top:371px" width="90" height="9"><g fill="#e01f26"><rect x="0" width="4" height="9"/><rect x="10" width="4" height="9"/><rect x="22" width="4" height="9"/><rect x="30" width="4" height="9"/><rect x="38" width="4" height="9"/><rect x="46" width="4" height="9"/><rect x="54" width="4" height="9"/><rect x="62" width="4" height="9"/><rect x="70" width="4" height="9"/><rect x="78" width="4" height="9"/></g></svg>
</section>

<div class="hero-photo" role="img" aria-label="Two colleagues in an office looking at a laptop together"></div>
<div class="badge"><strong>99%</strong><span>Happy Customers</span></div>
<div class="red-line" style="left:589px;top:532px;width:391px"></div>
<svg class="dashes" style="left:540px;top:535px" width="190" height="18"><g fill="#e01f26"><rect x="0" width="9" height="18"/><rect x="25" width="9" height="18"/><rect x="52" width="9" height="18"/><rect x="70" width="9" height="18"/><rect x="90" width="9" height="18"/><rect x="110" width="9" height="18"/><rect x="130" width="9" height="18"/><rect x="150" width="9" height="18"/><rect x="170" width="9" height="18"/></g></svg>

<section class="expertise">
  <h2>Our IT Expertise,<br>Your Success.</h2>
  <a class="btn btn-white" style="left:936px;top:86px;width:143px;height:34px">View all services
    <svg width="10" height="7" viewBox="0 0 10 7"><path d="M0 3.5h9M6 .5l3 3-3 3" fill="none" stroke="#2e3a44"/></svg></a>
  <svg class="dashes" style="left:912px;top:120px" width="92" height="9"><g fill="#fff"><rect x="0" width="4" height="9"/><rect x="12" width="4" height="9"/><rect x="24" width="4" height="9"/><rect x="34" width="4" height="9"/><rect x="44" width="4" height="9"/><rect x="54" width="4" height="9"/><rect x="64" width="4" height="9"/><rect x="74" width="4" height="9"/><rect x="84" width="4" height="9"/></g></svg>

  <article class="service-card" style="left:70px">
    <svg class="icon" width="54" height="54" viewBox="0 0 54 54" fill="none" stroke="#2e3a44" stroke-width="1.4"><circle cx="27" cy="27" r="12"/><path d="M27 4v11M27 39v11M4 27h11M39 27h11M11 11l8 8M35 35l8 8M43 11l-8 8M19 35l-8 8"/><rect x="22" y="25" width="10" height="8" stroke="#e01f26"/><path d="M24 25v-3a3 3 0 016 0v3" stroke="#e01f26"/></svg>
    <h3>Managed<br>Cybersecurity</h3>
    <p>60% of small businesses hit by a cyberattack go out of business within 6 months. But enterprise-level security...</p>
    <div class="rule"></div><div class="more">READ MORE &nbsp;→</div>
  </article>
  <article class="service-card featured" style="left:326px" aria-label="Managed Networks for MDUs, shown over a photo of apartment buildings">
    <svg class="icon" width="54" height="54" viewBox="0 0 54 54" fill="none" stroke="#fff" stroke-width="1.4"><circle cx="27" cy="13" r="9"/><path d="M23 13l3 3 5-6M27 22v8M12 30h30M12 30v6M27 30v6M42 30v6"/><rect x="5" y="36" width="14" height="8"/><rect x="20" y="36" width="14" height="8"/><rect x="35" y="36" width="14" height="8"/></svg>
    <h3>Managed Networks<br>for MDUs</h3>
    <p>High speed internet is now the number one amenity for multi-dwelling units. It needs to be fast, always online.</p>
    <div class="rule"></div><div class="more">READ MORE &nbsp;→</div>
  </article>
  <article class="service-card" style="left:580px">
    <svg class="icon" width="56" height="54" viewBox="0 0 56 54" fill="none" stroke="#2e3a44" stroke-width="1.4"><circle cx="12" cy="14" r="7"/><circle cx="12" cy="14" r="3"/><rect x="22" y="18" width="30" height="9"/><rect x="22" y="27" width="30" height="9"/><rect x="22" y="36" width="30" height="9"/><path d="M32 6v9M29 12l3 3 3-3M40 15V6M37 9l3-3 3 3" stroke="#e01f26"/></svg>
    <h3>Data Center<br>Services</h3>
    <p>Brivanoq Tech offers a full suite of data center services through our VaultFrame® brand.</p>
    <div class="rule"></div><div class="more">READ MORE &nbsp;→</div>
  </article>
  <article class="service-card" style="left:836px">
    <svg class="icon" width="54" height="54" viewBox="0 0 54 54" fill="none" stroke="#2e3a44" stroke-width="1.4"><rect x="14" y="4" width="26" height="34" rx="2"/><path d="M27 10l-6 10h12z" stroke="#e01f26"/><path d="M18 26h18M18 30h18M18 34h18M21 38v12M27 38v12M33 38v12"/></svg>
    <h3>Low Voltage<br>Wiring</h3>
    <p>To keep everyone connected with the outside world, modern buildings run on many different technologies.</p>
    <div class="rule"></div><div class="more">READ MORE &nbsp;→</div>
  </article>
</section>

<section class="about">
  <h2>About Brivanoq Tech</h2>
  <a class="btn btn-red" style="left:912px;top:1272px;width:115px;height:33px">Read more
    <svg width="10" height="7" viewBox="0 0 10 7"><path d="M0 3.5h9M6 .5l3 3-3 3" fill="none" stroke="#fff"/></svg></a>
  <svg class="dashes" style="left:888px;top:1305px" width="92" height="9"><g fill="#e01f26"><rect x="0" width="4" height="9"/><rect x="12" width="4" height="9"/><rect x="24" width="4" height="9"/><rect x="34" width="4" height="9"/><rect x="44" width="4" height="9"/><rect x="54" width="4" height="9"/><rect x="64" width="4" height="9"/><rect x="74" width="4" height="9"/><rect x="84" width="4" height="9"/></g></svg>
  <div class="about-photo" role="img" aria-label="Two women working together at computer monitors in a modern office"></div>
  <p class="about-text">Like most great businesses Brivanoq Tech began in a gargage during the summer of 1995 in Eastvale, SC. It was a part time venture by Marcus Delane and his business partner Owen Pratt. They had discovered an opportunity in technology sales and service after a combined 30 years at Halcrest Power in information technology. By 2000, the two set out on their own and were working on the venture full-time.</p>
  <div class="about-box">Today, the company has grown significantly and continues to do so. Brivanoq Tech provides services including multi-dwelling unit managed networks, data center services, low voltage wiring and local office IT support. Industries served include: retail, manufacturing, MDUs, hospitality, software development, medical, construction and more.</div>
  <div class="red-line" style="left:171px;top:1992px;width:516px"></div>
  <svg class="dashes" style="left:171px;top:1994px" width="140" height="14"><g fill="#e01f26"><rect x="0" width="6" height="14"/><rect x="18" width="6" height="14"/><rect x="36" width="6" height="14"/><rect x="50" width="6" height="14"/><rect x="64" width="6" height="14"/><rect x="78" width="6" height="14"/><rect x="92" width="6" height="14"/><rect x="106" width="6" height="14"/><rect x="120" width="6" height="14"/></g></svg>
</section>

<section class="data-center">
  <div class="dc-band">
    <h2>Your data center, your way</h2>
    <p>From single colocated servers to fully redundant virtualized environments.</p>
  </div>
  <div class="dc-photo" role="img" aria-label="Technician working between server racks lit with red cabling"></div>

  <div class="feature" style="top:2430px">
    <div class="circ"><svg width="38" height="26" viewBox="0 0 38 26" fill="none" stroke="#2e3a44" stroke-width="1.4"><path d="M2 10l8-6 6 3 6-3 8 6-12 12-6-5z"/><path d="M14 12l4 4M18 10l5 5" /><path d="M12 2l2 3M19 0v4M26 2l-2 3" stroke="#e01f26"/></svg></div>
    <h3>A True Partner</h3>
    <p>One size data center architecture does not fit all. We take the time to understand your specific requirements. We can provide as much or as little expertise as your organization requires for your specific project.</p>
  </div>
  <div class="feature" style="top:2527px">
    <div class="circ"><svg width="30" height="34" viewBox="0 0 30 34" fill="none" stroke="#2e3a44" stroke-width="1.4"><path d="M15 2L3 7v9c0 8 5 13 12 16 7-3 12-8 12-16V7z"/><path d="M9 17l4 4 8-9" stroke="#e01f26" stroke-width="1.8"/></svg></div>
    <h3>High Security</h3>
    <p>Our data center is a Tier III, standalone structure designed to withstand wind speeds up to 206mph. We have fully redundant power, cooling and internet connectivity. Biometrics are required to enter and visitors are always escorted.</p>
  </div>
  <div class="feature" style="top:2623px">
    <div class="circ"><svg width="32" height="34" viewBox="0 0 32 34" fill="none" stroke="#2e3a44" stroke-width="1.4"><path d="M10 6a13 13 0 1012 0"/><path d="M16 2v14" stroke="#e01f26" stroke-width="1.8"/><path d="M7 3l3 3-3 3"/></svg></div>
    <h3>Availability</h3>
    <p>The facility is powered by two separate utility feeds and a Dunmore diesel generator. We utilize multiple in-row cooling units, in-rack A/B power feeds and also have redundant, geographically diverse internet paths.</p>
  </div>
</section>

<section class="quote">
  <h2>Get a quote</h2>
  <p>Let's have a conversation to see how we can help with your data center needs.</p>
  <a class="btn btn-white" style="left:899px;top:78px;width:114px;height:34px">Contact us
    <svg width="10" height="7" viewBox="0 0 10 7"><path d="M0 3.5h9M6 .5l3 3-3 3" fill="none" stroke="#2e3a44"/></svg></a>
  <svg class="dashes" style="left:873px;top:112px" width="92" height="9"><g fill="#fff"><rect x="0" width="4" height="9"/><rect x="12" width="4" height="9"/><rect x="24" width="4" height="9"/><rect x="34" width="4" height="9"/><rect x="44" width="4" height="9"/><rect x="54" width="4" height="9"/><rect x="64" width="4" height="9"/><rect x="74" width="4" height="9"/><rect x="84" width="4" height="9"/></g></svg>
</section>

<footer class="site-footer">
  <div class="footer-brand"><span class="mark"></span>Brivanoq Tech</div>
  <nav class="footer-nav"><span>Home</span><span>|</span><span>Services</span><span>|</span><span>About</span><span>|</span><span>Contact</span></nav>
  <div class="footer-contact">
    <div><svg width="8" height="10" viewBox="0 0 8 10"><path d="M4 0a4 4 0 00-4 4c0 3 4 6 4 6s4-3 4-6a4 4 0 00-4-4z" fill="#e01f26"/></svg>48 Larkmoor Road | Eastvale, SC 29000</div>
    <div><svg width="9" height="9" viewBox="0 0 9 9"><path d="M1 0l2 2-1 2c1 1 2 2 3 3l2-1 2 2-1 1C4 9 0 5 0 1z" fill="#e01f26"/></svg>(555) 013-4827</div>
  </div>
  <div class="footer-rule"></div>
  <div class="copyright">2025 © Brivanoq Tech of SC, Inc.</div>
  <div class="legal"><span>Privacy Policy</span><span>|</span><span>Terms &amp; Conditions</span></div>
  <div class="to-top"><svg width="10" height="6" viewBox="0 0 10 6"><path d="M1 5l4-4 4 4" fill="none" stroke="#fff" stroke-width="1.5"/></svg></div>
</footer>

</body>
</html>
```